COVID-19 Accredited CME Impact Infographic

We want an infographic showing how much COVID-19 Continuing Medical Education we have accredited and its impact. Our website is at https://med.halvering.edu/cme/COVID19/education.html The attached document is intended to simply show the elements. You have complete freedom on design. We will be updating the numbers weekly so it is important that we have the files so that we can update it. This can be done in powerpoint, publisher, word, in-design, illustrator. Don't use crazy fonts that we wont have.

Target Market(s)

Internal to Halvering. We just want to show the impact of our work

Industry/Entity Type

Education

Requirements
Must have
• We must be able to update the numbers ourselves.

See attached document for the pieces that we want.

The sizes of the numbers in the attached are based on importance to us.
Nice to have
• Not mandatory but try to use these colors. https://med.halvering.edu/identity/color-palette.html

I was thinking that perhaps the big number could be done in traditional train. Like this: https://www.pictovane.com/image-illustration/flip-board-under-constuction-page-isolated-8803617452

```html
<!DOCTYPE html>
<html lang="en">
<head>
<meta charset="utf-8">
<title>COVID-19 CME Impact – Halvering Medicine</title>
<link href="https://fonts.googleapis.com/css2?family=Montserrat:wght@900&family=Open+Sans:ital,wght@0,600;0,700;1,600&family=Oswald:wght@600&display=swap" rel="stylesheet">
<style>
  :root{
    --page:#ffffff;
    --card:#f7f7f8;
    --band:#e7e8e9;
    --ink:#231f20;
    --ink-soft:#5e5a5a;
    --red:#c41e1e;
    --red-dark:#8c1515;
    --red-bright:#d63a24;
    --tile-top:#4e4a4a;
    --tile-bottom:#1f1c1c;
    --white:#ffffff;
  }
  *{box-sizing:border-box;margin:0;padding:0}
  html,body{width:1200px;height:796px;overflow:hidden;background:var(--page)}
  body{position:relative;font-family:"Open Sans",Arial,sans-serif}

  .card{
    position:absolute;left:137px;top:48px;width:923px;height:653px;
    background:var(--card);
    box-shadow:0 0 40px rgba(0,0,0,.16);
    overflow:hidden;
  }
  .header-band{position:absolute;left:0;top:0;width:100%;height:152px;background:var(--band)}
  .title{
    position:absolute;left:34px;top:36px;
    font-family:"Montserrat",Arial,sans-serif;font-weight:900;
    font-size:78px;letter-spacing:-1px;line-height:1;
  }
  .title .covid{
    background:linear-gradient(180deg,var(--ink-soft) 0%,var(--ink) 100%);
    -webkit-background-clip:text;background-clip:text;color:transparent;
  }
  .title .cme{color:var(--red-bright)}

  .virus-art{
    position:absolute;left:673px;top:0;width:250px;height:166px;
    background:radial-gradient(circle at 38% 48%,#9c1a16 0 22%,#d92a1f 23% 46%,rgba(217,42,31,0) 47%);
  }

  .divider{position:absolute;width:0;border-left:2px dotted var(--red-dark)}

  .label{
    position:absolute;height:29px;border-radius:5px;
    background:var(--red);color:var(--white);
    font-weight:600;font-size:17px;line-height:29px;text-align:center;white-space:nowrap;
  }
  .label.large{height:34px;font-size:21px;line-height:34px}

  .counter{position:absolute;display:flex}
  .tile{
    position:relative;width:37px;height:65px;border-radius:5px;
    background:linear-gradient(180deg,var(--tile-top) 0%,#2e2a2a 49%,#151313 50%,var(--tile-bottom) 100%);
    color:var(--white);
    font-family:"Oswald",Arial,sans-serif;font-weight:600;
    font-size:52px;line-height:65px;text-align:center;
  }
  .tile::after{
    content:"";position:absolute;left:0;right:0;top:50%;height:2px;margin-top:-1px;background:#0e0c0c;
  }
  .counter.small .tile{margin-right:7px}
  .counter.medium .tile{margin-right:7px}
  .counter.large .tile{width:42px;height:76px;font-size:62px;line-height:76px;margin-right:9.6px}
  .counter .tile:last-child{margin-right:0}

  .people-art{
    position:absolute;left:379px;top:496px;width:536px;height:157px;
    background:linear-gradient(90deg,#f7c325 0%,#7a5e8a 30%,#f26a5a 60%,#636363 100%);
  }
  .link-box{
    position:absolute;left:582px;top:618px;width:341px;height:24px;
    background:var(--white);border-radius:5px 0 0 5px;
    display:flex;align-items:center;gap:6px;padding-left:32px;
    color:var(--red-dark);font-weight:700;font-size:9.5px;
  }
  .link-box svg{position:absolute;left:32px;top:2px}
  .link-box span{margin-left:24px}

  .brand{
    position:absolute;left:35px;top:562px;display:flex;align-items:center;gap:10px;
    color:var(--red-dark);font-weight:700;font-size:30px;
  }
  .brand .mark{width:22px;height:22px;background:var(--red-dark)}

  .asof{
    position:absolute;left:898px;top:572px;
    transform:rotate(-90deg);transform-origin:left top;
    font-style:italic;font-weight:600;font-size:9px;color:var(--ink);white-space:nowrap;
  }
</style>
</head>
<body>
<main class="card">
  <div class="header-band"></div>
  <h1 class="title"><span class="covid">COVID-19</span><span class="cme">CME</span></h1>
  <div class="virus-art" role="img" aria-label="Illustration of red coronavirus particles"></div>

  <div class="divider" style="left:35px;top:175px;height:145px"></div>
  <div class="divider" style="left:193px;top:175px;height:145px"></div>
  <div class="divider" style="left:373px;top:175px;height:145px"></div>
  <div class="divider" style="left:623px;top:175px;height:145px"></div>
  <div class="divider" style="left:889px;top:175px;height:145px"></div>

  <div class="label" style="left:53px;top:188px;width:124px"># of states</div>
  <div class="label" style="left:213px;top:188px;width:141px"># of countries</div>
  <div class="label" style="left:407px;top:188px;width:183px"># of CME Learners</div>
  <div class="label" style="left:667px;top:188px;width:178px"># of live learners</div>

  <div class="counter small" style="left:73px;top:243px"><div class="tile">2</div><div class="tile">6</div></div>
  <div class="counter small" style="left:243px;top:243px"><div class="tile">1</div><div class="tile">2</div></div>
  <div class="counter medium" style="left:413px;top:243px"><div class="tile">5</div><div class="tile">8</div><div class="tile">7</div><div class="tile">9</div></div>
  <div class="counter medium" style="left:649px;top:243px"><div class="tile">2</div><div class="tile">3</div><div class="tile">0</div><div class="tile">9</div><div class="tile">8</div></div>

  <div class="divider" style="left:35px;top:348px;height:144px"></div>
  <div class="divider" style="left:562px;top:348px;height:144px"></div>
  <div class="divider" style="left:889px;top:348px;height:144px"></div>

  <div class="label large" style="left:141px;top:355px;width:315px"># of total on-demand views</div>
  <div class="label large" style="left:624px;top:355px;width:172px"># of Activities</div>

  <div class="counter large" style="left:122px;top:406px"><div class="tile">1</div><div class="tile">2</div><div class="tile">0</div><div class="tile">9</div><div class="tile">9</div><div class="tile">8</div><div class="tile">7</div></div>
  <div class="counter large" style="left:663px;top:406px"><div class="tile">2</div><div class="tile">3</div></div>

  <div class="people-art" role="img" aria-label="Illustration of four people wearing face masks"></div>

  <div class="brand"><div class="mark"></div>Halvering Medicine</div>

  <div class="link-box">
    <svg width="20" height="20" viewBox="0 0 20 20" aria-hidden="true">
      <path d="M4 18 L12 10 M12 10 L7 10 M12 10 L12 15" stroke="#8c1515" stroke-width="2.4" fill="none" stroke-linecap="round"/>
      <path d="M14 3 L14 6 M17 5 L15.5 6.5 M18 9 L16 9" stroke="#8c1515" stroke-width="1" stroke-linecap="round"/>
    </svg>
    <span>https://med.halvering.edu/cme/COVID19/education.html</span>
  </div>

  <p class="asof">Current as of 04/10/20</p>
</main>
</body>
</html>
```